Home Design company focused on remodel and enhancement of kitchens and bathroorms

I already have a logo designed by ArtHarbor, I now need a design for my business cards.
The company is in the remodeling and enhancement industry for homes, focusing on kitchens and bathrooms, however, we can remodel or enhance every room in a home, an office space, etc.

The company's name is VELMOR HOME DESIGN, LLC

We'll focus on clients in the Rio Grande Valley, Texas. Primarily McAllen, Edinburg, Pharr, Mission, Brownsville and South Padre Island.

The design on the business card should transmit reliability, professionalism anda bit of upscale design.

The logo is in black and white, and would like to keep it that way.

The information that needs to be printed in the business cards is:
Company's name: Velmor Home Design
Company's Logo (attached)
My name: Noel Bramwit
Address, phone and email:
2715 N Parkline Road, Ste 348
McAllen, TX 78501
(956) 555 0187
nbramwit@velmordesign.example
Website: velmordesign.example

```html
<!DOCTYPE html>
<html lang="en">
<head>
<meta charset="utf-8">
<title>Velmor Home Design — Business Card</title>
<link href="https://fonts.googleapis.com/css2?family=Poppins:wght@400;500;600;700&display=swap" rel="stylesheet">
<style>
  :root {
    --page: #ffffff;
    --ink: #161616;
    --paper: #ffffff;
    --tab: #c2c2c2;
    --icon-tile: #d6d6d6;
    --text-light: #ffffff;
  }
  * { margin: 0; padding: 0; box-sizing: border-box; }
  html, body {
    width: 708px; height: 1200px; overflow: hidden;
    background: var(--page);
    font-family: "Poppins", sans-serif;
  }
  .sheet {
    position: relative; width: 708px; height: 1200px;
    display: flex; justify-content: center; align-items: center; gap: 20px;
  }
  .card {
    position: relative; width: 322px; height: 564px;
    background: var(--ink); overflow: hidden;
    box-shadow: 0 8px 18px rgba(0,0,0,0.35);
  }
  .tab {
    position: absolute; left: 37px; width: 248px;
    background: var(--tab); border-radius: 14px 14px 0 0;
  }
  .tab--bottom { bottom: 0; height: 33px; }

  /* wordmark */
  .wordmark {
    position: absolute; left: 0; right: 0;
    text-align: center; font-weight: 400;
    letter-spacing: 0.32em; line-height: 1.05;
  }
  .wordmark span { display: block; }

  /* front */
  .front .wordmark { top: 190px; color: var(--text-light); font-size: 22px; }
  .front .name-band {
    position: absolute; top: 282px; left: 0; width: 100%; height: 28px;
    background: var(--paper); color: var(--ink);
    display: flex; align-items: center; justify-content: center;
    font-weight: 700; font-size: 17px; letter-spacing: 0.2em;
    padding-left: 0.2em;
  }
  .front .site {
    position: absolute; top: 320px; left: 0; width: 100%;
    text-align: center; color: var(--text-light);
    font-weight: 600; font-size: 15px;
  }

  /* back */
  .back .header {
    position: absolute; top: 0; left: 0; width: 100%; height: 182px;
    background: var(--paper);
  }
  .back .wordmark { top: 80px; color: var(--ink); font-size: 19px; }
  .back .tab--top { top: 171px; height: 11px; border-radius: 10px 10px 0 0; }
  .person {
    position: absolute; top: 206px; left: 0; width: 100%;
    text-align: center; color: var(--text-light);
    font-weight: 600; font-size: 19px; letter-spacing: 0.01em;
  }
  .person::after {
    content: ""; display: block; width: 52px; height: 2px;
    background: var(--text-light); margin: 4px auto 0;
  }
  .contact {
    position: absolute; top: 257px; left: 0; width: 100%;
    list-style: none; text-align: center; color: var(--text-light);
    font-size: 13.5px; font-weight: 400; line-height: 1.2;
  }
  .contact li { margin-bottom: 9px; }
  .contact .icon {
    display: block; width: 30px; height: 30px; margin: 0 auto 6px;
    background: var(--icon-tile); border-radius: 3px;
  }
  .contact .icon svg { width: 30px; height: 30px; display: block; }
</style>
</head>
<body>
<main class="sheet">

  <section class="card front" aria-label="Business card front">
    <div class="wordmark"><span>VELMOR</span><span>HOME</span><span>DESIGN</span></div>
    <div class="name-band">VELMOR HOME DESIGN</div>
    <p class="site">www.velmordesign.example</p>
    <div class="tab tab--bottom"></div>
  </section>

  <section class="card back" aria-label="Business card back">
    <div class="header">
      <div class="wordmark"><span>VELMOR</span><span>HOME</span><span>DESIGN</span></div>
      <div class="tab tab--top"></div>
    </div>
    <h1 class="person">NOEL BRAMWIT</h1>
    <ul class="contact">
      <li>
        <span class="icon"><svg viewBox="0 0 30 30" aria-hidden="true"><path d="M9 7.5c1-.8 2-.6 2.6.3l1.7 2.6c.5.8.3 1.6-.4 2.2l-1.1.9c.8 2 2.6 3.9 4.6 4.8l.9-1.1c.6-.7 1.5-.9 2.3-.4l2.6 1.7c.9.6 1 1.7.2 2.6l-1.2 1.3c-1 1-2.6 1.1-4 .4-3.8-1.9-6.8-5-8.6-8.7-.7-1.4-.5-3 .5-4z" fill="#161616"/></svg></span>
        (956) 555 0187
      </li>
      <li>
        <span class="icon"><svg viewBox="0 0 30 30" aria-hidden="true"><rect x="6.5" y="9" width="17" height="12" fill="none" stroke="#161616" stroke-width="1.6"/><path d="M6.5 9l8.5 7 8.5-7M6.5 21l6-5.5M23.5 21l-6-5.5" fill="none" stroke="#161616" stroke-width="1.4"/></svg></span>
        nbramwit@velmordesign.example
      </li>
      <li>
        <span class="icon"><svg viewBox="0 0 30 30" aria-hidden="true"><g fill="none" stroke="#161616" stroke-width="1.4"><circle cx="15" cy="15" r="8"/><ellipse cx="15" cy="15" rx="3.6" ry="8"/><path d="M7 15h16M8.2 11h13.6M8.2 19h13.6"/></g></svg></span>
        www.velmordesign.example
      </li>
      <li>
        <span class="icon"><svg viewBox="0 0 30 30" aria-hidden="true"><path d="M15 6.5a5.5 5.5 0 0 0-5.5 5.5c0 4 5.5 9.5 5.5 9.5s5.5-5.5 5.5-9.5A5.5 5.5 0 0 0 15 6.5z" fill="#161616"/><circle cx="15" cy="12" r="2.1" fill="#d6d6d6"/><path d="M9 21.5c0 1.2 2.7 2 6 2s6-.8 6-2" fill="none" stroke="#161616" stroke-width="1.4"/></svg></span>
        2715 N Parkline Road, Ste 348<br>McAllen, TX 78501
      </li>
    </ul>
    <div class="tab tab--bottom"></div>
  </section>

</main>
</body>
</html>
```